The Iron Forge of Bavarian Craft Beer

We are a small craft beer company from Bavaria. Family run and family brewed for 6 generations. We make great beers by hand, based on our experience, knowledge and intuition. We believe in craft, but in the same time we believe that the Bavarian breweries have remained stuck in the past. They have become old-fashioned and dusty, and so many are in danger of extinction.

But we want to become the leaders of the iron forge of Bavarian craft. Our beers are brewed naturally, matured in more than 6 weeks and fully according to the best Bavarian standards. But we will add an edgy, modern twist and sometimes even break the famous German purity law -- when the biermaister believes he can achieve something extraordinary doing it!

We will start all fresh with a new name: IBF (meaning "Iron Bavarian Forge") or just IF ("Iron Forge" of Bavarian Craft) whichever inspires you better.

We will have a range of traditional and new beers, so the design must allow for a multicoloured range that will be easily recognised on shelf. The names of 3 variants: Hellesbier (blonde lager), Urbock (dark lager) and Weissbier (white wheat beer).

Brand archetype: Magician/Outlaw. We are the real craftsmen of beer, but our traditional way is so threatened by the advance of the big corporations, that we must get extra creative and break out of the rules they are imposing, to break out of the crowd.

Reason: I am extending the deadline to be able to make some research. Thank you.

Target Market(s)

Beer lovers in Europe. 30-45 yo men, working hard in some corporation and and earning a good income, who want to reward themselves in the evenings with a special treat. They believe that quality comes form hard work and that has a price - and authentic Bavarian craft is a good answer to their belief. They dress casual or semi-casual, they may appear quite conformists but actually want an escape from the corporate routine into something more edgy, more raw and masculine.

Industry/Entity Type

It Company

Requirements
Must have
• While the name and attitude is fresh, we need to use our existing packaging lines, so in the attachments you can find the limited choice bottles we can use. See which one inspires you most and work on that one.
• To me it would be great if we can take the ugly Euro glass and give our brand a crafty look with the labels.
• Which reminds me: label substrate is now paper, or at most metal coated paper - it would be ideal to stay, although if something really fantastic comes out with transparency on plastic or glass, we would also consider an investment.
• As far as label dimensions, we can be relatively flexible, although two points to note:
• -- the labels need to be quite simple in terms of shape, otherwise they will get destroyed by the packaging line
• -- the labels must fit over straight lines in the bottle (cylindrical or conical), can't put label over more complex curves
• Other text:
• -- name is IBF or IF whichever inspires you most
• -- should use one of the variant names (Hellesbier, Urbock or Weissbier") to indicate what beer is in the bottle. The variant should be highligted beyond text with some background color
• -- should use "Iron Forge of Bavarian Craft" as explanation.
• -- can also use "Bavarian Malt, Bavarian Hops, Bavarian craft" as slogan
Nice to have
• While the design must be modern and edgy, it needs to retain an element of hand-craft and nature - we believe the combination of modernity and nature / handcraft creates a good visual tension.
Should not have
• Other glass shapes, other glass openings than in the photos.
• Backlabel with ingredients aso

```html
<!DOCTYPE html>
<html lang="en">
<head>
<meta charset="utf-8">
<title>Hellesbier Label – IBF</title>
<link rel="stylesheet" href="https://fonts.googleapis.com/css2?family=Abril+Fatface&family=Caveat:wght@500&display=swap">
<style>
  :root {
    --bg: #ffffff;
    --green-light: #b4d24a;
    --green-mid: #8dba2e;
    --green-deep: #4f7f1a;
    --rim: #f7f6ee;
    --band: #fbfaf3;
    --ink: #1d1a16;
    --brand-red: #c4201c;
  }
  html, body {
    margin: 0;
    width: 807px;
    height: 1200px;
    overflow: hidden;
    background: var(--bg);
  }
  .canvas {
    width: 807px;
    height: 1200px;
    display: block;
  }
  .variant-name {
    font-family: "Abril Fatface", "Playfair Display", serif;
    fill: var(--ink);
  }
  .slogan {
    font-family: "Caveat", cursive;
    font-weight: 500;
    fill: var(--ink);
  }
  .brand-name {
    font-family: "Abril Fatface", "Playfair Display", serif;
    fill: var(--brand-red);
  }
  .explanation {
    font-family: "Abril Fatface", "Playfair Display", serif;
    fill: var(--rim);
    letter-spacing: 2px;
  }
</style>
</head>
<body>
<svg class="canvas" viewBox="0 0 807 1200" xmlns="http://www.w3.org/2000/svg">
  <defs>
    <radialGradient id="label-burst" cx="50%" cy="45%" r="60%">
      <stop offset="0%" stop-color="var(--green-light)"/>
      <stop offset="70%" stop-color="var(--green-mid)"/>
      <stop offset="100%" stop-color="var(--green-deep)"/>
    </radialGradient>
    <clipPath id="label-shape">
      <ellipse cx="403" cy="600" rx="288" ry="418"/>
    </clipPath>
  </defs>

  <g class="label">
    <ellipse class="label-rim" cx="403" cy="600" rx="300" ry="430" fill="var(--rim)" stroke="var(--green-deep)" stroke-width="3"/>
    <ellipse class="label-field" cx="403" cy="600" rx="288" ry="418" fill="url(#label-burst)" role="img" aria-label="Green radiating sunburst background"/>

    <g class="brand-badge">
      <circle cx="403" cy="330" r="112" fill="var(--rim)" stroke="var(--green-deep)" stroke-width="5"/>
      <text class="brand-name" x="403" y="358" font-size="84" text-anchor="middle">IBF</text>
    </g>

    <g class="variant-band" clip-path="url(#label-shape)">
      <rect x="100" y="500" width="607" height="120" fill="var(--band)"/>
      <line x1="100" y1="506" x2="707" y2="506" stroke="var(--ink)" stroke-width="3"/>
      <line x1="100" y1="614" x2="707" y2="614" stroke="var(--ink)" stroke-width="3"/>
      <rect x="100" y="620" width="607" height="10" fill="var(--green-deep)"/>
    </g>
    <text class="variant-name" x="403" y="592" font-size="92" text-anchor="middle" textLength="530" lengthAdjust="spacingAndGlyphs">HELLESBIER</text>

    <text class="slogan" x="403" y="690" font-size="36" text-anchor="middle" textLength="450" lengthAdjust="spacingAndGlyphs">Bavarian Malt, Bavarian Hops, Bavarian craft</text>

    <g class="explanation-block">
      <line x1="213" y1="775" x2="593" y2="775" stroke="var(--rim)" stroke-width="2"/>
      <text class="explanation" x="403" y="822" font-size="34" text-anchor="middle" textLength="400" lengthAdjust="spacingAndGlyphs">IRON FORGE OF BAVARIAN CRAFT</text>
      <line x1="213" y1="845" x2="593" y2="845" stroke="var(--rim)" stroke-width="2"/>
    </g>
  </g>
</svg>
</body>
</html>
```